Membership Card for our Survival Company

We need a membership card design, front and back for our VIP Membership program. Membership card must be branded with our logo and convey the idea of survivalism.
All members will receive this physical, plastic card with embossed Full Name and unique Membership ID.
ID formatting: "VIP-XXXXXXX"
See example image here:
https://media.brightorbalo.com/7k/52e9a1c3b08d44f6a7c1d29e3b0f57/VIP-Membership-Card1-Reflect.png
Note, this is just an example. We do not require you to follow the size, format, image, etc. The only things that must be included are the:
1) Logo
2) Full Name
3) Membership ID as per the provided format
Any more questions, please let me know.
It Company
Full Name
VIP-XXXXXXX

```html
<!DOCTYPE html>
<html lang="en">
<head>
<meta charset="utf-8">
<title>WildEndure VIP Membership Card</title>
<link rel="stylesheet" href="https://fonts.googleapis.com/css2?family=Bree+Serif&family=Cinzel:wght@700&family=Share+Tech+Mono&display=swap">
<style>
  :root {
    --page-bg: #d9d6d1;
    --card-bg: #2a2119;
    --card-bg-deep: #1a1410;
    --photo-light: #d2ad6e;
    --photo-mid: #8a6536;
    --photo-dark: #3b2b1a;
    --brand-gold: #f4b12c;
    --brand-circle: #f29a1c;
    --emboss-gold: #e8cf98;
    --emboss-shadow: #5a3f1c;
  }
  * { box-sizing: border-box; margin: 0; padding: 0; }
  html, body {
    width: 1200px;
    height: 900px;
    overflow: hidden;
    background: var(--page-bg);
  }
  .canvas {
    position: relative;
    width: 1200px;
    height: 900px;
  }
  .member-card {
    position: absolute;
    left: 290px;
    width: 620px;
    height: 391px;
    border-radius: 20px;
    overflow: hidden;
    background: linear-gradient(100deg, var(--card-bg) 40%, var(--card-bg-deep) 100%);
    box-shadow: 0 10px 24px rgba(0, 0, 0, 0.25);
  }
  .member-card--named { top: 34px; }
  .member-card--vip { top: 475px; }
  .card-photo {
    position: absolute;
    left: 0;
    top: 0;
    width: 300px;
    height: 100%;
    background:
      radial-gradient(ellipse 150px 240px at 90px 190px, var(--photo-light) 0%, var(--photo-mid) 50%, rgba(138, 101, 54, 0) 100%),
      linear-gradient(90deg, var(--photo-dark) 0%, var(--photo-mid) 40%, rgba(42, 33, 25, 0) 100%);
  }
  .brand {
    position: absolute;
    left: 130px;
    top: 58px;
    display: flex;
    align-items: center;
    gap: 12px;
  }
  .brand-mark {
    width: 62px;
    height: 62px;
    border-radius: 50%;
    background: var(--brand-circle);
  }
  .brand-name {
    font-family: "Bree Serif", serif;
    font-size: 46px;
    color: var(--brand-gold);
    line-height: 1;
  }
  .card-title {
    position: absolute;
    left: 110px;
    top: 158px;
    font-family: "Cinzel", serif;
    font-weight: 700;
    font-size: 36px;
    letter-spacing: 1px;
    color: var(--emboss-gold);
    text-shadow: 1px 2px 0 var(--emboss-shadow);
    white-space: nowrap;
  }
  .member-id {
    position: absolute;
    left: 150px;
    top: 236px;
    font-family: "Share Tech Mono", monospace;
    font-size: 40px;
    letter-spacing: 4px;
    color: var(--emboss-gold);
    text-shadow: 1px 2px 0 var(--emboss-shadow);
    white-space: nowrap;
  }
</style>
</head>
<body>
  <main class="canvas">
    <section class="member-card member-card--named">
      <div class="card-photo" role="img" aria-label="Survivor in a hooded jacket and gas mask with coiled rope, against a hazy ruined skyline in warm sepia tones"></div>
      <div class="brand">
        <span class="brand-mark"></span>
        <span class="brand-name">WildEndure</span>
      </div>
      <p class="card-title">MARCUS HALVERN</p>
      <p class="member-id">VIP-0482157</p>
    </section>

    <section class="member-card member-card--vip">
      <div class="card-photo" role="img" aria-label="Survivor in a hooded jacket and gas mask with coiled rope, against a hazy ruined skyline in warm sepia tones"></div>
      <div class="brand">
        <span class="brand-mark"></span>
        <span class="brand-name">WildEndure</span>
      </div>
      <p class="card-title">VIP MEMBERSHIP CARD</p>
      <p class="member-id">VIP-0482157</p>
    </section>
  </main>
</body>
</html>
```